Banner Ad Design Project

I need a banner add that will be used as the main graphical image for an internet radio show. My picture needs to be in the final product as well as the following information:

Morning Ledger (larger letters, this is the name of the show)

Every Tuesdays at 1pm PST
With your host Owen Hartley
Sponsored by brightvK7

Also, the color scheme and graphics should work with the website www.brightvk7.example

I have also included 2 examples of another radio show called Velvet Orbit....I like the way they look.
Updates

I have uploaded new logos, that now include the words Radio Show.  Please update designs to include this new logo, and REMOVE any other instance of RADIO SHOW in your design.  Also, we would love to see some variation on the sponsored by area.  Can you also show us: Brought to you by (instead of Sponsored by)

Also, it should be Every Tuesday  NOT Tuesdays

Target Market(s)

CEOs, Top Executives

Industry/Entity Type

Internet

Requirements
Must have
• Morning Ledger (larger letters, this is the name of the show)

Every Tuesday at 1pm PST
With your host Owen Hartley
Sponsored by brightvK7 (use the logo I provided)

(use only 1 of my pictures, choose the one you think works best with your design)

The image should be a rectangle and longer than tall.

Also, the Morning Ledger logo should be in the design. A dark and light version has been included, based on your design.
Should not have
• Radio Show as a separate area. We have now made that a part of the logo

```html
<!DOCTYPE html>
<html lang="en">
<head>
<meta charset="utf-8">
<title>Morning Ledger – Every Tuesday at 1pm PST</title>
<link rel="stylesheet" href="https://fonts.googleapis.com/css2?family=Alegreya+Sans:wght@400;800&display=swap">
<style>
  :root {
    --page: #ffffff;
    --teal: #1a7b8c;
    --teal-band: rgba(150, 200, 210, 0.28);
    --navy: #1f2360;
    --white: #ffffff;
    --photo-light: #ede2cf;
    --photo-mid: #c9b18e;
    --photo-dark: #7a6448;
  }
  html, body {
    margin: 0;
    padding: 0;
    width: 1200px;
    height: 878px;
    overflow: hidden;
    background: var(--page);
    font-family: "Alegreya Sans", sans-serif;
  }
  .banner {
    position: absolute;
    left: 77px;
    top: 91px;
    width: 1051px;
    height: 701px;
    background: var(--teal);
    overflow: hidden;
  }
  .show-title {
    position: absolute;
    left: 20px;
    top: 8px;
    width: 1010px;
    height: 140px;
  }
  .show-title text {
    font-family: "Alegreya Sans", sans-serif;
    font-weight: 800;
    font-size: 124px;
    fill: var(--navy);
  }
  .band {
    position: absolute;
    left: 0;
    width: 718px;
    background: var(--teal-band);
  }
  .band--schedule { top: 312px; height: 93px; }
  .band--host { top: 495px; height: 40px; }
  .band--sponsor { top: 619px; height: 48px; }
  .schedule, .host, .sponsor {
    position: absolute;
    margin: 0;
    color: var(--white);
    font-weight: 400;
    white-space: nowrap;
    line-height: 1;
  }
  .schedule {
    left: 41px;
    top: 320px;
    font-size: 53px;
  }
  .host {
    left: 175px;
    top: 497px;
    font-size: 30px;
  }
  .sponsor {
    left: 184px;
    top: 624px;
    font-size: 31px;
  }
  .host strong, .sponsor strong {
    font-weight: 800;
  }
  .sponsor strong { font-size: 35px; }
  .host-photo {
    position: absolute;
    left: 718px;
    top: 211px;
    width: 333px;
    height: 490px;
    background: radial-gradient(ellipse at 45% 30%, var(--photo-light) 0%, var(--photo-mid) 55%, var(--photo-dark) 100%);
  }
</style>
</head>
<body>
  <main class="banner">
    <svg class="show-title" viewBox="0 0 1010 140" aria-label="Morning Ledger">
      <text x="0" y="118" textLength="1000" lengthAdjust="spacingAndGlyphs">MORNING LEDGER</text>
    </svg>

    <div class="band band--schedule"></div>
    <div class="band band--host"></div>
    <div class="band band--sponsor"></div>

    <p class="schedule">Every Tuesday at 1pm PST</p>
    <p class="host">With your host <strong>Owen Hartley</strong></p>
    <p class="sponsor">Powered by <strong>brightvK7</strong></p>

    <div class="host-photo" role="img" aria-label="Portrait photo of host Owen Hartley in a suit, seated against a warm beige backdrop"></div>
  </main>
</body>
</html>
```